Marrowgate Auctions Business Cards Design Needed

I need a business card design that is modern looking - double sided (maybe just my logo on the back, but open to suggestions) - the overall design is up to you. I want it to be easy to read - not over the top flashy. I already have a company logo which I uploaded so that needs to be used. The colors of my logo are the colors I want on the card... so blue and gray (do need to match the logo colors).

Requirements
Must have
• Would like the card to be sleek, modern and easy to ready

```html
<!DOCTYPE html>
<html lang="en">
<head>
<meta charset="utf-8">
<title>Marrowgate Auctions – Business Card</title>
<link href="https://fonts.googleapis.com/css2?family=Open+Sans:ital,wght@0,400;0,700;1,700&display=swap" rel="stylesheet">
<style>
  :root {
    --frame-gray: #d3d7dc;
    --card-navy: #1d3f66;
    --wave-slate: #5d6773;
    --brand-blue: #4aa3ff;
    --ink-light: #ffffff;
    --ink-soft: #e3e8ee;
    --icon-fill: #eef1f4;
    --paper: #ffffff;
  }
  * { margin: 0; padding: 0; box-sizing: border-box; }
  html, body { width: 1200px; height: 730px; overflow: hidden; background: var(--paper); }
  body { font-family: "Open Sans", Arial, sans-serif; }

  .card {
    position: relative;
    width: 1200px;
    height: 730px;
    background: var(--frame-gray);
  }
  .card-face {
    position: absolute;
    left: 40px; top: 41px;
    width: 1094px; height: 642px;
    background: var(--card-navy);
    overflow: hidden;
  }
  .wave { position: absolute; inset: 0; width: 100%; height: 100%; }

  .brand {
    position: absolute;
    left: 0; right: 0; top: 84px;
    display: flex; justify-content: center; align-items: center; gap: 26px;
  }
  .brand-mark { width: 118px; height: 118px; background: var(--brand-blue); flex: none; }
  .brand-name {
    font-weight: 700; font-size: 56px; line-height: 1.05; letter-spacing: 1px;
    color: var(--brand-blue); text-transform: uppercase;
  }
  .brand-name span { display: block; }

  .tagline {
    position: absolute; left: 0; right: 0; top: 272px;
    text-align: center;
    font-style: italic; font-weight: 700; font-size: 29px;
    color: var(--ink-light);
    text-shadow: 1px 1px 2px rgba(0,0,0,.45);
  }

  .person { position: absolute; left: 71px; top: 466px; color: var(--ink-light); }
  .person-name { font-weight: 700; font-size: 29px; line-height: 1.2; }
  .person-role { font-size: 21px; line-height: 1.3; color: var(--ink-soft); }

  .contact-list { position: absolute; left: 655px; top: 446px; width: 362px; list-style: none; }
  .contact-item {
    display: flex; justify-content: space-between; align-items: center;
    height: 42px; font-size: 24px; color: var(--ink-light);
  }
  .contact-icon { width: 22px; height: 22px; flex: none; }
</style>
</head>
<body>
<div class="card">
  <div class="card-face">
    <svg class="wave" viewBox="0 0 1094 642" preserveAspectRatio="none" aria-hidden="true">
      <path d="M423 642 C480 530 560 455 680 440 C820 432 960 430 1094 413 L1094 642 Z" fill="var(--wave-slate)"/>
    </svg>

    <div class="brand">
      <span class="brand-mark"></span>
      <p class="brand-name"><span>Marrowgate</span><span>Auctions</span></p>
    </div>

    <p class="tagline">Improving Charity Auctions Nationwide</p>

    <div class="person">
      <p class="person-name">Corin Ashby</p>
      <p class="person-role">Owner/President- Auctioneer</p>
    </div>

    <ul class="contact-list">
      <li class="contact-item">
        <svg class="contact-icon" viewBox="0 0 24 24" aria-label="Phone">
          <circle cx="12" cy="12" r="12" fill="var(--icon-fill)"/>
          <path d="M8 6.5l2 0 1 3-1.4 1.2a7 7 0 0 0 3.7 3.7L14.5 13l3 1v2a1.5 1.5 0 0 1-1.6 1.5A10 10 0 0 1 6.5 8.1 1.5 1.5 0 0 1 8 6.5z" fill="var(--wave-slate)"/>
        </svg>
        <span>555-014-2837</span>
      </li>
      <li class="contact-item">
        <svg class="contact-icon" viewBox="0 0 24 24" aria-label="Email">
          <circle cx="12" cy="12" r="12" fill="var(--icon-fill)"/>
          <rect x="6" y="8" width="12" height="8" rx="1" fill="var(--wave-slate)"/>
          <path d="M6.5 8.5L12 12.5 17.5 8.5" stroke="var(--icon-fill)" stroke-width="1.2" fill="none"/>
        </svg>
        <span>marrowgatebids@mail.com</span>
      </li>
      <li class="contact-item">
        <svg class="contact-icon" viewBox="0 0 24 24" aria-label="Website">
          <circle cx="12" cy="12" r="12" fill="var(--icon-fill)"/>
          <circle cx="12" cy="12" r="6" fill="none" stroke="var(--wave-slate)" stroke-width="1.4"/>
          <ellipse cx="12" cy="12" rx="2.6" ry="6" fill="none" stroke="var(--wave-slate)" stroke-width="1.2"/>
          <path d="M6 12h12M7 9h10M7 15h10" stroke="var(--wave-slate)" stroke-width="1.1"/>
        </svg>
        <span>http://bidrevival.com/</span>
      </li>
    </ul>
  </div>
</div>
</body>
</html>
```